Disaster Recovery firm needs design for impactful Door Hanger flyer

We need the design for a 4.25X11 inch door hanger with die-cut included for the hanger. The hangers will be hung on the door medium to high net worth clientele's residential homes. They need to reference the event Hurricane Ondine and speak to the issues that people have resulting from the storm and the benefits of our service. We will provide the sales language and bullet points.

Target Market(s)

Residential homeowners

Font styles to use
Sans Serif

Colors
3277b5
ec1f27
cee9f5
cedeed

Requirements
Must have
• Photos that include visual references to hurricane damage,
bullet points to convey the benefits of the service,
call to action, & company & local office contact information
Nice to have
• Great graphic design with layers & topics
Should not have
• Pictures of money, promises of "cash" or "no risk" and certain other violations of written statutes& compliance

```html
<!DOCTYPE html>
<html lang="en">
<head>
<meta charset="UTF-8">
<title>Tidewell Recovery Partners – Door Hanger</title>
<link href="https://fonts.googleapis.com/css2?family=Poppins:ital,wght@0,600;0,700;0,800;1,800&family=Courier+Prime&display=swap" rel="stylesheet">
<style>
  :root {
    --page-bg: #e6e7e9;
    --brand-blue: #3277b5;
    --deep-blue: #1c4a6d;
    --edge-blue: #245f86;
    --brand-red: #ec1f27;
    --ink-red: #c8202a;
    --pale-blue: #cee9f5;
    --mist-blue: #cedeed;
    --white: #ffffff;
    --navy-text: #1b2a3a;
    --sky-top: #8d8a88;
    --sky-mid: #b9b6b2;
    --roof-tone: #5a4a4e;
  }
  * { box-sizing: border-box; margin: 0; padding: 0; }
  html, body { width: 1200px; height: 800px; overflow: hidden; }
  body {
    background: var(--page-bg);
    font-family: "Poppins", Arial, sans-serif;
    position: relative;
  }
  .door-hanger {
    position: absolute;
    left: 450px;
    top: 12px;
    width: 300px;
    height: 776px;
    overflow: hidden;
    background: var(--deep-blue);
    box-shadow: 0 6px 18px rgba(0,0,0,0.18);
  }
  .door-hanger::before,
  .door-hanger::after {
    content: "";
    position: absolute;
    top: 0;
    bottom: 0;
    width: 6px;
    background: var(--edge-blue);
    z-index: 5;
  }
  .door-hanger::before { left: 0; }
  .door-hanger::after { right: 0; }

  .storm-photo {
    position: absolute;
    left: 0; top: 0;
    width: 300px; height: 440px;
    background: linear-gradient(160deg, var(--sky-top) 0%, var(--sky-mid) 30%, #9c9088 48%, var(--roof-tone) 70%, #3e3438 100%);
  }
  .panel-shape { position: absolute; left: 0; top: 0; }

  .die-cut-hole {
    position: absolute;
    left: 105px; top: 39px;
    width: 90px; height: 90px;
    border-radius: 50%;
    background: var(--page-bg);
    z-index: 6;
  }

  .brand-badge {
    position: absolute;
    left: 85px; top: 312px;
    width: 130px; height: 130px;
    border-radius: 50%;
    background: var(--white);
    display: flex;
    align-items: center;
    justify-content: center;
    text-align: center;
    z-index: 4;
  }
  .brand-name {
    font-weight: 700;
    font-size: 13px;
    line-height: 1.2;
    color: var(--navy-text);
    letter-spacing: 0.5px;
  }

  .headline {
    position: absolute;
    left: 0; right: 0; top: 448px;
    text-align: center;
    color: var(--white);
    font-weight: 800;
    font-size: 37px;
    line-height: 40px;
    letter-spacing: -0.5px;
    text-shadow: 0 3px 4px rgba(0,0,0,0.45);
    z-index: 4;
  }

  .service-list {
    position: absolute;
    left: 10px; top: 536px;
    list-style: none;
    font-family: "Courier Prime", "Courier New", monospace;
    font-size: 10.5px;
    line-height: 18.8px;
    color: var(--white);
    z-index: 4;
  }
  .service-list li::before {
    content: "";
    display: inline-block;
    width: 6px; height: 6px;
    border-radius: 50%;
    background: var(--brand-red);
    margin-right: 4px;
    vertical-align: 1px;
  }

  .column-divider {
    position: absolute;
    left: 148px; top: 538px;
    width: 2px; height: 140px;
    background: var(--white);
    z-index: 4;
  }

  .promise {
    position: absolute;
    left: 157px; top: 534px;
    font-style: italic;
    font-weight: 800;
    font-size: 20.5px;
    line-height: 25px;
    color: var(--white);
    z-index: 4;
  }

  .call-to-action {
    position: absolute;
    left: 0; right: 0; top: 684px;
    text-align: center;
    font-weight: 700;
    font-size: 19px;
    color: var(--white);
    letter-spacing: 0.3px;
    z-index: 4;
  }

  .phone-bar {
    position: absolute;
    left: 0; right: 0; top: 728px;
    height: 48px;
    background: linear-gradient(180deg, var(--white) 0%, var(--mist-blue) 100%);
    z-index: 4;
  }
  .phone-bar__tab {
    position: absolute;
    left: 0; top: 6px;
    width: 72px; height: 36px;
    background: var(--ink-red);
  }
  .phone-bar__icon {
    position: absolute;
    left: 36px; top: 3px;
    width: 42px; height: 42px;
  }
  .phone-bar__number {
    position: absolute;
    left: 86px; top: 4px;
    font-weight: 800;
    font-size: 29px;
    line-height: 40px;
    color: var(--ink-red);
    letter-spacing: -0.3px;
  }
</style>
</head>
<body>
  <main class="door-hanger">
    <div class="storm-photo" role="img" aria-label="Photo of a storm-damaged house with a torn-open roof under dark hurricane clouds"></div>

    <svg class="panel-shape" width="300" height="776" viewBox="0 0 300 776" aria-hidden="true">
      <defs>
        <linearGradient id="panelBlue" x1="0" y1="0" x2="0" y2="1">
          <stop offset="0" stop-color="#3277b5"/>
          <stop offset="0.55" stop-color="#26608f"/>
          <stop offset="1" stop-color="#1c4a6d"/>
        </linearGradient>
      </defs>
      <polygon points="0,324 300,425 300,776 0,776" fill="url(#panelBlue)"/>
      <polygon points="0,324 300,425 300,440 0,340" fill="#3277b5" opacity="0.6"/>
    </svg>

    <div class="die-cut-hole"></div>

    <div class="brand-badge">
      <span class="brand-name">TIDEWELL<br>RECOVERY<br>PARTNERS</span>
    </div>

    <h1 class="headline">THE STORM<br>CAUGHT YOU</h1>

    <ul class="service-list">
      <li>HAIL DAMAGE</li>
      <li>WIND DAMAGE</li>
      <li>STORM DAMAGE</li>
      <li>ROOF INSPECTIONS</li>
      <li>ROOF REPAIRS</li>
      <li>GUTTER REPAIRS</li>
      <li>SIDING REPAIRS</li>
      <li>WINDOW REPAIRS</li>
    </ul>

    <div class="column-divider"></div>

    <p class="promise">Make The<br>Best<br>Decision For<br>Your Roof<br>And Home</p>

    <p class="call-to-action">CALL US TODAY</p>

    <div class="phone-bar">
      <div class="phone-bar__tab"></div>
      <svg class="phone-bar__icon" viewBox="0 0 42 42" aria-hidden="true">
        <circle cx="21" cy="21" r="19" fill="#c8202a" stroke="#ffffff" stroke-width="3"/>
        <path d="M15 11c1-1 2.5-1 3.2 0l2 3c.6.9.4 2-.4 2.7l-1.3 1.1c.9 2 2.6 3.8 4.6 4.7l1.1-1.3c.7-.8 1.8-1 2.7-.4l3 2c1 .7 1 2.2 0 3.2l-1.6 1.6c-1.3 1.3-3.3 1.5-4.9.6-4.3-2.4-7.8-5.9-10.1-10.2-.9-1.6-.6-3.6.7-4.9z" fill="#ffffff"/>
      </svg>
      <span class="phone-bar__number">555.014.2290</span>
    </div>
  </main>
</body>
</html>
```